Cafe Menu Required

We need a menu for our coffee shop.
I would like something very much the same as what I have attached.

I have attached a word doc with the items needed on the menu.

I have also attached our logo

I would like to print these on A3 size poster

Industry/Entity Type

Cafe

```html
<!DOCTYPE html>
<html lang="en">
<head>
<meta charset="utf-8">
<title>Kettle Row Coffee Menu</title>
<link href="https://fonts.googleapis.com/css2?family=Arimo:wght@400;700&family=Parisienne&display=swap" rel="stylesheet">
<style>
  :root {
    --cream: #f3ead6;
    --cream-edge: #e6d9bd;
    --red: #c8432f;
    --red-dark: #a8321f;
    --ink: #1d1b19;
    --leader: #6e655a;
    --silhouette: #262019;
    --cup-tone: #9a7b5c;
    --white: #ffffff;
  }
  * { margin: 0; padding: 0; box-sizing: border-box; }
  html, body { width: 872px; height: 1200px; overflow: hidden; }
  body {
    background: var(--cream);
    font-family: "Arimo", Arial, sans-serif;
    color: var(--ink);
  }
  .menu {
    position: relative;
    width: 872px;
    height: 1200px;
    background: radial-gradient(ellipse at center, var(--cream) 55%, var(--cream-edge) 100%);
    overflow: hidden;
  }
  .foliage-band { position: absolute; left: 0; top: 0; width: 872px; height: 300px; }
  .ground-band { position: absolute; left: 0; bottom: 0; width: 872px; height: 150px; }
  .brand {
    position: absolute; left: 52px; top: 140px;
    display: flex; align-items: center; gap: 12px;
  }
  .brand-mark { width: 26px; height: 26px; background: var(--white); }
  .brand-name { font-weight: 700; font-size: 34px; color: var(--white); letter-spacing: 1px; }
  .menu-title {
    position: absolute; right: 70px; top: 20px;
    font-family: "Parisienne", cursive;
    color: var(--white); font-size: 76px; line-height: 0.95; text-align: left;
  }
  .menu-title span { display: block; }
  .menu-title span + span { margin-left: 48px; }
  .tagline {
    position: absolute; left: 0; right: 0; top: 378px;
    text-align: center; font-weight: 700; font-size: 29px; letter-spacing: 0.5px;
    padding-left: 150px;
  }
  .cup-icons { position: absolute; left: 370px; top: 425px; width: 300px; height: 80px; }
  .column { position: absolute; }
  .column-hot { left: 146px; top: 530px; width: 360px; }
  .column-extras { left: 537px; top: 530px; width: 300px; }
  .column-cold { left: 537px; top: 808px; width: 300px; }
  .section-title {
    font-weight: 700; font-size: 19px; text-transform: uppercase;
    text-align: center; margin-bottom: 22px;
  }
  .items { list-style: none; }
  .item {
    display: flex; align-items: baseline;
    font-size: 17px; height: 41px;
  }
  .item-leader {
    flex: 1; margin: 0 4px;
    border-bottom: 2px dotted var(--leader);
    transform: translateY(-4px);
  }
</style>
</head>
<body>
<main class="menu">
  <svg class="foliage-band" role="img" aria-label="Red autumn foliage canopy across the top" viewBox="0 0 872 300" preserveAspectRatio="none">
    <defs>
      <linearGradient id="foliage" x1="0" y1="0" x2="0" y2="1">
        <stop offset="0" stop-color="#a8321f"/>
        <stop offset="1" stop-color="#c8432f"/>
      </linearGradient>
    </defs>
    <path fill="url(#foliage)" d="M0 0 H872 V210 C840 240 810 200 780 230 C740 270 700 220 660 250 C620 285 590 230 550 255 C510 280 470 240 430 265 C400 285 360 250 330 270 C290 300 250 255 220 280 C180 300 150 260 110 285 C70 300 40 265 0 290 Z"/>
  </svg>

  <div class="brand">
    <span class="brand-mark"></span>
    <span class="brand-name">Kettle Row</span>
  </div>

  <h1 class="menu-title"><span>Coffee</span><span>Menu</span></h1>

  <p class="tagline">COFFEE – CATERING – FOOD TO GO</p>

  <svg class="cup-icons" role="img" aria-label="Three coffee cup and pot icons" viewBox="0 0 300 80">
    <rect x="10" y="10" width="280" height="64" rx="10" fill="var(--cup-tone)" opacity="0.35"/>
  </svg>

  <section class="column column-hot">
    <h2 class="section-title">Hot Beverages</h2>
    <ul class="items">
      <li class="item"><span>Espresso</span><span class="item-leader"></span><span>3.5</span></li>
      <li class="item"><span>Picolo</span><span class="item-leader"></span><span>3.5</span></li>
      <li class="item"><span>Short Macchiato</span><span class="item-leader"></span><span>4.0</span></li>
      <li class="item"><span>Long Macchiato</span><span class="item-leader"></span><span>4.5</span></li>
      <li class="item"><span>Latte</span><span class="item-leader"></span><span>4/4.5/5.5</span></li>
      <li class="item"><span>Cappuccino</span><span class="item-leader"></span><span>4/4.5/5.5</span></li>
      <li class="item"><span>Flat White</span><span class="item-leader"></span><span>4/4.50/5.50</span></li>
      <li class="item"><span>Long Black</span><span class="item-leader"></span><span>4/4.50/5.50</span></li>
      <li class="item"><span>Hot Chocolate</span><span class="item-leader"></span><span>4/4.50/5.50</span></li>
      <li class="item"><span>White Hot Chocolate</span><span class="item-leader"></span><span>4/4.50/5.50</span></li>
      <li class="item"><span>Mocha</span><span class="item-leader"></span><span>4.5/5/6.0</span></li>
      <li class="item"><span>White Choc Mocha</span><span class="item-leader"></span><span>4.5/5/6.0</span></li>
      <li class="item"><span>Chai Latte</span><span class="item-leader"></span><span>4.5/5/6.0</span></li>
      <li class="item"><span>Dirty Chai</span><span class="item-leader"></span><span>5.0/5.5/6.5</span></li>
      <li class="item"><span>Selection of Teas</span><span class="item-leader"></span><span>3.8</span></li>
    </ul>
  </section>

  <section class="column column-extras">
    <h2 class="section-title">Extras</h2>
    <ul class="items">
      <li class="item"><span>Extra Shot</span><span class="item-leader"></span><span>0.5</span></li>
      <li class="item"><span>Decaf</span><span class="item-leader"></span><span>0.5</span></li>
      <li class="item"><span>Syrups – Caramel/Hazelnut/Vanilla</span><span class="item-leader"></span><span>0.5</span></li>
      <li class="item"><span>Soy</span><span class="item-leader"></span><span>0.5</span></li>
      <li class="item"><span>Lactose free</span><span class="item-leader"></span><span>0.5</span></li>
    </ul>
  </section>

  <section class="column column-cold">
    <h2 class="section-title">Cold Beverages</h2>
    <ul class="items">
      <li class="item"><span>Iced Latte</span><span class="item-leader"></span><span>4.5</span></li>
      <li class="item"><span>Iced Long Black</span><span class="item-leader"></span><span>4.5</span></li>
      <li class="item"><span>Iced Coffee w/ice cream</span><span class="item-leader"></span><span>6.0</span></li>
      <li class="item"><span>Iced Chocolate w/ice cream</span><span class="item-leader"></span><span>6.0</span></li>
      <li class="item"><span>Coffee Frappe</span><span class="item-leader"></span><span>6.0</span></li>
      <li class="item"><span>Mango Frappe</span><span class="item-leader"></span><span>6.0</span></li>
    </ul>
  </section>

  <svg class="ground-band" role="img" aria-label="Dark tree and shrub silhouettes along the bottom" viewBox="0 0 872 150" preserveAspectRatio="none">
    <path fill="var(--silhouette)" d="M0 20 C30 10 60 40 90 70 C110 95 130 110 160 120 C260 135 400 128 520 120 C600 112 650 90 700 60 C740 35 780 20 830 40 C850 48 862 30 872 25 V150 H0 Z"/>
  </svg>
</main>
</body>
</html>
```